Accounting services

Looking for a Business card & Logo design

company name - LUMEN ACCOUNTING & TAXATION SOLUTIONS

name - Corwin Pell

position - Accountant / Business Consultant

email - "undecided"

Tel : (868) 512-4873 / (868) 587-2196

**PUT THESE TO THE BACK**
Accounting - VAT * INCOME/CORP TAX * RETURNS

REGISTRATION - VAT * NIS * Company Registration/Business Plan

Industry/Entity Type

Business

```html
<!DOCTYPE html>
<html lang="en">
<head>
<meta charset="UTF-8">
<title>Lumen Accounting &amp; Taxation Solutions — Business Card</title>
<link href="https://fonts.googleapis.com/css2?family=Tinos:wght@400;700&display=swap" rel="stylesheet">
<style>
  :root {
    --backdrop: #e9e6e1;
    --card-black: #0b0b0b;
    --card-sheen: #2a2a2a;
    --gold: #e2b21a;
    --gold-light: #f1cc3a;
    --gold-deep: #c8940c;
    --white: #f4f4f4;
    --ink: #1a1a1a;
  }
  * { margin: 0; padding: 0; box-sizing: border-box; }
  html, body {
    width: 1200px; height: 902px; overflow: hidden;
    background: var(--backdrop);
    font-family: "Tinos", "Times New Roman", serif;
  }
  .canvas { position: relative; width: 1200px; height: 902px; }
  .card {
    position: absolute; width: 700px; height: 400px; overflow: hidden;
    background: linear-gradient(125deg, var(--card-black) 0%, var(--card-sheen) 38%, var(--card-black) 62%, var(--card-black) 100%);
    box-shadow: 0 14px 30px rgba(0,0,0,.35);
    color: var(--white);
  }
  .card-back { left: 60px; top: 40px; }
  .card-front { left: 440px; top: 462px; }
  .card svg.bands { position: absolute; inset: 0; width: 700px; height: 400px; }

  .back-title {
    position: absolute; left: 34px; right: 34px; top: 38px;
    font-size: 26px; font-weight: 400; letter-spacing: .3px; white-space: nowrap;
  }
  .services-label {
    position: absolute; left: 60px; top: 112px; font-size: 16px;
  }
  .services {
    position: absolute; left: 170px; top: 112px; list-style: none;
    font-size: 16px; line-height: 26px;
  }

  .front-title {
    position: absolute; left: 70px; top: 74px; width: 360px;
    font-size: 28px; font-weight: 400; line-height: 36px; text-align: center; white-space: nowrap;
  }
  .contacts { position: absolute; left: 450px; top: 112px; list-style: none; font-size: 16px; line-height: 30px; }
  .contacts li { display: flex; align-items: center; gap: 12px; }
  .contacts svg { width: 18px; height: 18px; flex: none; }
  .role {
    position: absolute; left: 480px; top: 246px; color: var(--ink);
    font-size: 12px; line-height: 15px; letter-spacing: .3px;
  }
  .holder-name {
    position: absolute; left: 150px; top: 322px; color: var(--ink);
    font-size: 30px; font-weight: 400;
  }
</style>
</head>
<body>
<div class="canvas">

  <section class="card card-back" aria-label="Card back">
    <svg class="bands" viewBox="0 0 700 400" aria-hidden="true">
      <defs>
        <linearGradient id="goldBack" x1="0" y1="0" x2="1" y2="0">
          <stop offset="0" stop-color="var(--gold-light)"/>
          <stop offset="1" stop-color="var(--gold-deep)"/>
        </linearGradient>
      </defs>
      <polygon points="0,322 440,322 448,300 0,300" fill="var(--card-black)"/>
      <polygon points="0,316 432,316 436,306 0,306" fill="var(--white)"/>
      <polygon points="0,342 440,342 462,278 700,278 700,400 0,400" fill="url(#goldBack)"/>
    </svg>
    <h2 class="back-title">LUMEN ACCOUNTING &amp; TAXATION SOLUTIONS</h2>
    <p class="services-label">SIRVISE</p>
    <ul class="services">
      <li>ACCOUNTING - VAT</li>
      <li>RETURNS</li>
      <li>INCOME/CORP TAX</li>
      <li>REGISTRATION - VAT</li>
      <li>NIS</li>
      <li>COMPANY REGISTRATION/BUSINESS PLAN</li>
    </ul>
  </section>

  <section class="card card-front" aria-label="Card front">
    <svg class="bands" viewBox="0 0 700 400" aria-hidden="true">
      <defs>
        <linearGradient id="goldFront" x1="0" y1="0" x2="1" y2="0">
          <stop offset="0" stop-color="var(--gold-light)"/>
          <stop offset="1" stop-color="var(--gold-deep)"/>
        </linearGradient>
      </defs>
      <polygon points="330,236 700,236 700,282 402,282" fill="var(--white)"/>
      <polygon points="0,262 316,262 392,300 700,300 700,400 0,400" fill="url(#goldFront)"/>
    </svg>
    <h1 class="front-title">LUMEN ACCOUNTING<br>&amp;<br>TAXATION SOLUTIONS</h1>
    <ul class="contacts">
      <li>
        <svg viewBox="0 0 20 20"><circle cx="10" cy="10" r="9" fill="none" stroke="var(--white)" stroke-width="1.4"/><path d="M7 5.5l1.6 2.4-1 1.1c.6 1.3 1.5 2.2 2.8 2.8l1.1-1 2.4 1.6-.9 1.8c-3.6-.3-6.7-3.4-7-7z" fill="var(--white)"/></svg>
        (868) 512-4873
      </li>
      <li>
        <svg viewBox="0 0 20 20"><circle cx="10" cy="10" r="9" fill="none" stroke="var(--white)" stroke-width="1.4"/><path d="M7 5.5l1.6 2.4-1 1.1c.6 1.3 1.5 2.2 2.8 2.8l1.1-1 2.4 1.6-.9 1.8c-3.6-.3-6.7-3.4-7-7z" fill="var(--white)"/></svg>
        (868) 587-2196
      </li>
      <li>
        <svg viewBox="0 0 20 20"><circle cx="10" cy="10" r="9" fill="none" stroke="var(--white)" stroke-width="1.4"/><rect x="5.5" y="7" width="9" height="6.5" fill="var(--white)"/><path d="M5.5 7l4.5 3.5L14.5 7" fill="none" stroke="var(--card-black)" stroke-width="1"/></svg>
        info@lumenaccounts.com
      </li>
    </ul>
    <p class="role">ACCOUNTANT<br>BUSINESS CONSULTANT</p>
    <p class="holder-name">Corwin Pell</p>
  </section>

</div>
</body>
</html>
```